New Bicycle shop business card

Hi!
I'm looking for a business card for my new proffesional bike mechanics shop. This shop is only for fixing broken bikes and not selling bikes.
Peferbly a modern and sleek and modern design.
Colors: black, grey, red, white
Information:
Name: Rijwielwerkplaats Vanhoutem
Shop owner: Bart Vanhoutem & Sanne Maertens
Website: www.rijwielwerkplaats-vanhoutem.be
Email: info@rijwielwerkplaats-vanhoutem.be
Phone number: +32471902386
Street adres: Kerkweg 64
9970 Oostmoere
Slogan/shop information: Herstellingen van alle merken.
Logo: see files.
Target Market(s)
People who seek a mechanic to fix or upgrade their bikes.
Contact Information for Business Card
Information:
Website: info@rijwielwerkplaats-vanhoutem.be
9970 Oostmoere
Logo: see files.

```html
<!DOCTYPE html>
<html lang="nl">
<head>
<meta charset="utf-8">
<title>Rijwielwerkplaats Vanhoutem – Business card</title>
<link rel="stylesheet" href="https://fonts.googleapis.com/css2?family=Roboto:wght@400;500;700&display=swap">
<style>
  :root {
    --backdrop: #3a3a3c;
    --card: #241e1d;
    --red: #d3303f;
    --white: #ececec;
    --grey: #a9a9a9;
    --font: "Roboto", Arial, sans-serif;
  }
  * { margin: 0; padding: 0; box-sizing: border-box; }
  html, body {
    width: 1200px; height: 901px; overflow: hidden;
    background: var(--backdrop);
    font-family: var(--font);
  }
  .sheet {
    width: 1200px; height: 901px;
    display: flex; flex-direction: column;
    align-items: center; justify-content: center; gap: 60px;
  }
  .card {
    position: relative;
    width: 600px; height: 343px;
    background: var(--card);
    box-shadow: 0 12px 30px rgba(0,0,0,.45);
    overflow: hidden;
  }
  /* brand name block */
  .brand {
    display: flex; align-items: center; gap: 14px;
  }
  .brand-mark {
    width: 34px; height: 34px; background: var(--red); flex: none;
  }
  .brand-name {
    font-weight: 700; color: var(--white);
    text-transform: uppercase; letter-spacing: .08em; line-height: 1.15;
  }
  /* front */
  .card-front { display: flex; align-items: center; justify-content: center; }
  .card-front .brand-name { font-size: 22px; }
  /* back */
  .card-back { padding: 38px 44px; }
  .card-back .brand-name { font-size: 15px; }
  .card-back .brand-mark { width: 26px; height: 26px; }
  .contact { margin-top: 34px; color: var(--white); font-size: 13.5px; line-height: 1.45; }
  .contact-name { color: var(--red); font-size: 22px; font-weight: 500; margin-bottom: 2px; }
  .contact-owner { color: var(--grey); }
  .contact-address { margin-top: 10px; }
  .contact-lines { margin-top: 10px; list-style: none; }
  .contact-lines li { display: flex; align-items: center; gap: 10px; }
  .contact-lines svg { width: 12px; height: 12px; fill: var(--red); flex: none; }
  .slogan-band {
    position: absolute; left: 0; right: 0; bottom: 0; height: 28px;
    background: var(--red); color: var(--white);
    font-size: 12.5px; display: flex; align-items: center;
    justify-content: flex-end; padding-right: 44px;
  }
</style>
</head>
<body>
<main class="sheet">
  <section class="card card-front" aria-label="Front of business card">
    <div class="brand">
      <span class="brand-mark"></span>
      <span class="brand-name">Rijwielwerkplaats<br>Vanhoutem</span>
    </div>
  </section>

  <section class="card card-back" aria-label="Back of business card">
    <div class="brand">
      <span class="brand-mark"></span>
      <span class="brand-name">Rijwielwerkplaats<br>Vanhoutem</span>
    </div>
    <div class="contact">
      <p class="contact-name">Rijwielwerkplaats Vanhoutem</p>
      <p class="contact-owner">Shop owner: Bart Vanhoutem &amp; Sanne Maertens</p>
      <p class="contact-address">Kerkweg 64<br>9970 Oostmoere</p>
      <ul class="contact-lines">
        <li>
          <svg viewBox="0 0 24 24" aria-hidden="true"><path d="M6.6 10.8a15 15 0 0 0 6.6 6.6l2.2-2.2a1 1 0 0 1 1-.25 11.4 11.4 0 0 0 3.6.57 1 1 0 0 1 1 1V20a1 1 0 0 1-1 1A17 17 0 0 1 3 4a1 1 0 0 1 1-1h3.5a1 1 0 0 1 1 1c0 1.25.2 2.45.57 3.6a1 1 0 0 1-.25 1z"/></svg>
          +32471902386
        </li>
        <li>
          <svg viewBox="0 0 24 24" aria-hidden="true"><path d="M2 5h20v14H2zm2 2v.4l8 5.1 8-5.1V7zm0 2.8V17h16V9.8l-8 5.1z"/></svg>
          info@rijwielwerkplaats-vanhoutem.be
        </li>
        <li>
          <svg viewBox="0 0 24 24" aria-hidden="true"><path d="M12 2a10 10 0 1 0 0 20 10 10 0 0 0 0-20zm6.9 6h-2.9a15 15 0 0 0-1.4-3.6A8 8 0 0 1 18.9 8zM12 4a13 13 0 0 1 1.9 4h-3.8A13 13 0 0 1 12 4zM4.3 14a8 8 0 0 1 0-4h3.4a16 16 0 0 0 0 4zm.8 2h2.9a15 15 0 0 0 1.4 3.6A8 8 0 0 1 5.1 16zM8 8H5.1a8 8 0 0 1 4.3-3.6A15 15 0 0 0 8 8zm4 12a13 13 0 0 1-1.9-4h3.8A13 13 0 0 1 12 20zm2.3-6H9.7a14 14 0 0 1 0-4h4.6a14 14 0 0 1 0 4zm.3 5.6A15 15 0 0 0 16 16h2.9a8 8 0 0 1-4.3 3.6zM16.3 14a16 16 0 0 0 0-4h3.4a8 8 0 0 1 0 4z"/></svg>
          www.rijwielwerkplaats-vanhoutem.be
        </li>
      </ul>
    </div>
    <div class="slogan-band">Herstellingen van alle merken.</div>
  </section>
</main>
</body>
</html>
```